Blue Mesa Fuels-Ethanol Plant-Business Card Design

We are looking to incorporate a new logo on a new business card design. Can be vertical or horizontal.
We currently produce a variety of feed products as well as pharmaceutical grade ethanol that can be used in hand sanitizers, medications, and vaccines and hospitals for sterilization. We are also the first company to incorporate Carbon Capture and Storage (CCS) which takes all of our CO2 emissions and injects it deep into the earth-about 6400 feet below our facility.
For our logo we are looking for something professional, detailed, yet simple looking that can be used for all areas of our company. Something 'timeless' that can be used for many years to come, no matter what future projects our company takes on.
Industry/Entity Type
Corn/Ethanol Plant
Contact Information for Business Card
First & Last Name, Title, E-Mail, Office Phone: 555.210.4471 Ext. 1000 , Fax: 555.210.4472, Cell: 555.386.9025, Email: Info@bluemesafuels.example, Address: 5149 Route 4 N PO Box 27 Richardton, ND 50917, Website: www.bluemesafuels.example
Look and feel

```html
<!DOCTYPE html>
<html lang="en">
<head>
<meta charset="utf-8">
<title>Blue Mesa Fuels – Business Card</title>
<link href="https://fonts.googleapis.com/css2?family=Cinzel:wght@500&family=Poppins:wght@300;400;500&display=swap" rel="stylesheet">
<style>
  :root {
    --green: #2f9a05;
    --green-dark: #27860a;
    --white: #ffffff;
    --ink: #222222;
    --grey: #a9a9a9;
    --rule: #bdbdbd;
    --backdrop: #bfbfbf;
  }
  * { margin: 0; padding: 0; box-sizing: border-box; }
  html, body { width: 1200px; height: 800px; overflow: hidden; }
  body {
    background: var(--backdrop);
    font-family: "Poppins", sans-serif;
    position: relative;
  }
  .card {
    position: absolute;
    top: 245px;
    width: 540px;
    height: 310px;
    overflow: hidden;
    box-shadow: 0 10px 28px rgba(0,0,0,0.25);
  }
  .card--front { left: 45px; background: var(--white); }
  .card--back { left: 615px; background: var(--green); }

  /* front */
  .brand { position: absolute; text-align: center; }
  .card--front .brand { left: 20px; top: 40px; width: 230px; }
  .brand__mark {
    display: block;
    margin: 0 auto 14px;
    border-radius: 50%;
  }
  .card--front .brand__mark { width: 120px; height: 120px; border: 7px solid var(--green); }
  .brand__name { font-weight: 400; line-height: 1; white-space: nowrap; }
  .card--front .brand__name { color: var(--green); font-size: 28px; }
  .brand__tag { letter-spacing: 0.18em; font-weight: 400; }
  .card--front .brand__tag { color: #555; font-size: 11px; margin-top: 5px; }

  .divider {
    position: absolute; left: 268px; top: 52px;
    width: 1px; height: 170px; background: var(--rule);
  }
  .contact { position: absolute; left: 290px; top: 46px; color: var(--ink); }
  .contact__name {
    font-family: "Cinzel", serif; font-weight: 500;
    color: var(--green); font-size: 25px; line-height: 1;
  }
  .contact__name .initial { font-size: 31px; }
  .contact__title { font-size: 14px; margin-top: 4px; }
  .contact__list { list-style: none; margin-top: 16px; font-size: 13px; line-height: 1.35; }
  .contact__list li { display: flex; align-items: flex-start; gap: 8px; margin-bottom: 4px; }
  .contact__list svg { width: 13px; height: 13px; flex: none; margin-top: 3px; fill: var(--green); }

  .band { position: absolute; left: 0; bottom: 0; width: 540px; height: 64px; }
  .band__url {
    position: absolute; right: 26px; bottom: 16px;
    color: var(--white); font-size: 14px; letter-spacing: 0.02em;
  }

  /* back */
  .card--back .brand { left: 0; top: 50px; width: 100%; }
  .card--back .brand__mark { width: 150px; height: 150px; border: 8px solid var(--white); margin-bottom: 20px; }
  .card--back .brand__name { color: var(--white); font-size: 38px; }
  .card--back .brand__tag { color: var(--white); font-size: 15px; margin-top: 6px; }
</style>
</head>
<body>

<section class="card card--front">
  <div class="brand">
    <span class="brand__mark"></span>
    <div class="brand__name">Blue Mesa Fuels</div>
    <div class="brand__tag">ETHANOL PLANT</div>
  </div>

  <div class="divider"></div>

  <div class="contact">
    <div class="contact__name"><span class="initial">J</span>ONATHAN <span class="initial">S</span>MITH</div>
    <div class="contact__title">Managing Director</div>
    <ul class="contact__list">
      <li>
        <svg viewBox="0 0 24 24" aria-hidden="true"><path d="M6.6 10.8a15 15 0 0 0 6.6 6.6l2.2-2.2a1 1 0 0 1 1-.25 11.4 11.4 0 0 0 3.6.57 1 1 0 0 1 1 1V20a1 1 0 0 1-1 1A17 17 0 0 1 3 4a1 1 0 0 1 1-1h3.5a1 1 0 0 1 1 1c0 1.25.2 2.45.57 3.57a1 1 0 0 1-.25 1z"/></svg>
        <span>000 XXX 0000</span>
      </li>
      <li>
        <svg viewBox="0 0 24 24" aria-hidden="true"><path d="M2 5h20v14H2z M2 5l10 8 10-8" stroke="#fff" stroke-width="1.5"/></svg>
        <span>email@websitename.com</span>
      </li>
      <li>
        <svg viewBox="0 0 24 24" aria-hidden="true"><path d="M12 2a7 7 0 0 0-7 7c0 5 7 13 7 13s7-8 7-13a7 7 0 0 0-7-7zm0 9.5A2.5 2.5 0 1 1 12 6.5a2.5 2.5 0 0 1 0 5z"/></svg>
        <span>Adress line here with<br>country pincode 000021</span>
      </li>
    </ul>
  </div>

  <svg class="band" viewBox="0 0 540 64" preserveAspectRatio="none" aria-hidden="true">
    <path d="M0,54 H318 Q328,54 330,44 L333,24 Q335,14 346,14 H540 V64 H0 Z" fill="var(--green)"/>
    <path d="M0,47 H312 Q321,47 323,38 L326,22" fill="none" stroke="var(--grey)" stroke-width="6"/>
  </svg>
  <div class="band__url">www.websitename.com</div>
</section>

<section class="card card--back">
  <div class="brand">
    <span class="brand__mark"></span>
    <div class="brand__name">Blue Mesa Fuels</div>
    <div class="brand__tag">ETHANOL PLANT</div>
  </div>
</section>

</body>
</html>
```